Residential technology services business card

Looking for a simple, catchy, slightly fun business card design.

We are a residential technology service provider (computer repair, tablet repair, training, etc). We are a fun, upbeat, yet professional company that is very skilled at our job.

I will upload our logo in a sec, thinking that it should be the only thing on the front side of the card, with maybe a punch line as well... maybe not. Maybe the punchline can find a place on the back. You be the judge.

Backside should be minimal in terms of information. I need two variations: one that will only have our website and phone and one that will also include a persons name (and position), personal e-mail and personal phone.

Well, you're the designer, figure out the best way to place all above mentioned items.

Colors are white, black, green (as in logo), plus whatever else you think needs adding (if any).

It must be clear to people what we do (provide computer services, tablet services)... without using generic pictures of computers and tablets, unless it 's something original.

We want something original! But do note that the card will be printed on standard size business card paper, so no funky shapes please.

Thanks!!!

Residential

Requirements
Must have
• Logo, website, phone.
2nd variation also must include space for persons name, personal phone and email.

```html
<!DOCTYPE html>
<html lang="en">
<head>
<meta charset="UTF-8">
<title>ByteNest Business Cards</title>
<link rel="stylesheet" href="https://fonts.googleapis.com/css2?family=Arimo:wght@400;700&family=Questrial&display=swap">
<style>
  :root {
    --page-bg: #e9e7e3;
    --silver-light: #f4f4f4;
    --silver-mid: #d9d9d9;
    --silver-dark: #b9b9b9;
    --ink: #1c1c1c;
    --green-deep: #14631f;
    --green: #2f8f2c;
    --green-bright: #6cc04a;
    --band: #eef0ec;
    --white: #ffffff;
  }
  * { margin: 0; padding: 0; box-sizing: border-box; }
  html, body {
    width: 1200px;
    height: 900px;
    overflow: hidden;
    background: var(--page-bg);
  }
  .canvas {
    position: relative;
    width: 1200px;
    height: 900px;
  }
  .card {
    position: absolute;
    width: 560px;
    height: 320px;
    border-radius: 26px;
    overflow: hidden;
    box-shadow: 0 12px 30px rgba(0,0,0,0.25);
  }

  /* Front */
  .card-front {
    left: 110px;
    top: 80px;
    background: radial-gradient(ellipse at 45% 40%, var(--silver-light) 0%, var(--silver-mid) 60%, var(--silver-dark) 100%);
    display: flex;
    flex-direction: column;
    align-items: center;
    justify-content: center;
  }
  .brand {
    display: flex;
    align-items: center;
    gap: 14px;
  }
  .brand-dot {
    width: 34px;
    height: 34px;
    border-radius: 50%;
    background: var(--green-bright);
  }
  .brand-name {
    font-family: "Arimo", Arial, sans-serif;
    font-weight: 700;
    font-size: 70px;
    letter-spacing: -2px;
    color: var(--ink);
  }
  .front-web {
    margin-top: 16px;
    font-family: "Arimo", Arial, sans-serif;
    font-weight: 700;
    font-size: 20px;
    color: var(--green-deep);
  }
  .services {
    margin-top: 18px;
    font-family: "Questrial", "Century Gothic", sans-serif;
    font-size: 21px;
    color: var(--ink);
    letter-spacing: 0.5px;
  }
  .services .sep { margin: 0 8px; }

  /* Back */
  .card-back {
    left: 530px;
    top: 480px;
    background: radial-gradient(ellipse at 40% 10%, var(--green-bright) 0%, var(--green) 45%, var(--green-deep) 100%);
  }
  .back-brand {
    position: absolute;
    right: 34px;
    top: 34px;
    display: flex;
    align-items: center;
    gap: 10px;
  }
  .back-brand .brand-dot {
    width: 22px;
    height: 22px;
    background: var(--white);
  }
  .back-brand .brand-name {
    font-size: 46px;
    color: var(--white);
    letter-spacing: -1px;
  }
  .id-band {
    position: absolute;
    left: 0;
    right: 0;
    top: 148px;
    height: 76px;
    background: linear-gradient(90deg, rgba(238,240,236,0) 0%, rgba(238,240,236,0.85) 35%, var(--band) 100%);
    text-align: right;
    padding: 10px 30px 0 0;
    font-family: "Arimo", Arial, sans-serif;
    color: var(--ink);
  }
  .person-name { font-weight: 700; font-size: 20px; }
  .person-role { font-size: 15px; }
  .person-email { font-size: 20px; margin-top: 2px; }
  .contact {
    position: absolute;
    right: 30px;
    bottom: 22px;
    text-align: right;
    font-family: "Arimo", Arial, sans-serif;
    font-size: 18px;
    line-height: 1.35;
    color: var(--white);
  }
  .contact b { font-weight: 700; }
</style>
</head>
<body>
<main class="canvas">
  <section class="card card-front">
    <div class="brand">
      <span class="brand-dot"></span>
      <span class="brand-name">ByteNest</span>
    </div>
    <p class="front-web">www.bytenest.com</p>
    <p class="services">COMPUTER REPAIR<span class="sep">|</span>TABLET REPAIR<span class="sep">|</span>TRAINING</p>
  </section>

  <section class="card card-back">
    <div class="back-brand">
      <span class="brand-dot"></span>
      <span class="brand-name">ByteNest</span>
    </div>
    <div class="id-band">
      <p><span class="person-name">Dana Porter</span> <span class="person-role">| President</span></p>
      <p class="person-email">dporter@bytenest.com</p>
    </div>
    <div class="contact">
      <p><b>P</b> (555) 210-0101 | <b>F</b> (555) 210-0102 | <b>M</b> (555) 210-0103</p>
      <p>4120 Cedar Ridge Road #12, Springfield, TX 75001</p>
    </div>
  </section>
</main>
</body>
</html>
```